property investment and development company needs a website

we need a website that looks professional and portrays trust for people looking to us to buy their house or investors looking to invest or joint venture with us.
We are based in the west midlands in the UK.
we deal mainly with residential housing, house to flats conversions, HMO's (houses in multiple ocupancy).
we require the website as a first point of contact with potential sellers, renters and investors so links or contact details that are easy to access or see would be good.
I have had logos designed by a brisk easel member and these can be used as guidance for the colour and style of the site.
Target Market(s)
joint venture investment partners, people looking to sell their house, people looking to rent from us.
Coding
Coded - Design and coding required
Number of Pages Required
3 page
Requirements
Must have
- project a professional appearance
- visable contact details

```html
<!DOCTYPE html>
<html lang="en">
<head>
<meta charset="utf-8">
<title>Calder Homes</title>
<link href="https://fonts.googleapis.com/css2?family=Cinzel:wght@400;700&family=Montserrat:wght@700&family=Raleway:wght@400;500&display=swap" rel="stylesheet">
<style>
:root{
  --gold:#c8a86a;
  --gold-dark:#a98a4c;
  --gold-band:#c9ad73;
  --ink:#1f2433;
  --text:#555;
  --muted:#888;
  --panel:#1b1b1b;
  --footer:#111;
  --white:#fff;
}
*{box-sizing:border-box;margin:0;padding:0}
html,body{width:1200px;height:2880px;overflow:hidden;background:var(--white)}
body{position:relative;font-family:'Raleway',sans-serif;color:var(--text)}
.abs{position:absolute}
.btn{position:absolute;display:flex;align-items:center;justify-content:center;border-radius:30px;
  background:linear-gradient(180deg,#d2b57a,var(--gold-dark));color:var(--white);
  font-family:'Cinzel',serif;font-weight:700;font-size:21px;letter-spacing:1px}
/* header */
.site-header{position:absolute;left:0;top:0;width:1200px;height:104px;background:var(--white)}
.brand{position:absolute;left:76px;top:24px;display:flex;align-items:center;gap:12px}
.brand-mark{width:44px;height:44px;border:2px solid var(--gold)}
.brand-name{font-family:'Cinzel',serif;font-size:28px;line-height:30px;color:var(--gold-dark);letter-spacing:1px}
.nav{position:absolute;top:33px;right:0;display:flex;align-items:center;font-size:15px;color:#333;letter-spacing:.5px}
.nav a{color:inherit;text-decoration:none}
.nav-home{position:absolute;left:582px;top:33px;width:94px;height:41px;border-radius:22px;background:linear-gradient(180deg,#d2b57a,var(--gold-dark));color:#fff;font-size:15px;display:flex;align-items:center;justify-content:center}
/* hero */
.hero{position:absolute;left:0;top:104px;width:1200px;height:572px;
  background:linear-gradient(180deg,#5c6a92 0%,#7b7c9a 40%,#8a7f7e 70%,#4a4f44 100%)}
.hero-title{position:absolute;left:79px;top:196px;font-family:'Montserrat',sans-serif;font-weight:700;font-size:68px;line-height:68px;color:#fff;letter-spacing:-1px}
.hero-sub{position:absolute;left:79px;top:347px;font-size:18px;line-height:27px;color:#fff}
.dots{position:absolute;right:32px;top:230px;display:flex;flex-direction:column;gap:9px}
.dots span{width:15px;height:15px;border-radius:50%;background:#fff}
.dots span.on{background:transparent;border:2px solid var(--gold)}
/* band */
.call-band{position:absolute;left:0;top:676px;width:1200px;height:94px;background:var(--gold-band)}
.call-band p{position:absolute;left:79px;top:33px;font-style:italic;font-size:25px;color:#fff;font-weight:500}
.call-num{position:absolute;right:79px;top:25px;display:flex;align-items:center;gap:10px;font-family:'Cinzel',serif;font-weight:700;font-size:31px;color:#1a1a1a}
/* welcome */
.welcome{position:absolute;left:0;top:770px;width:1200px;text-align:center}
.welcome h3{margin-top:70px;font-family:'Cinzel',serif;font-weight:700;font-size:23px;color:var(--ink);letter-spacing:1px}
.welcome h2{margin-top:8px;font-family:'Cinzel',serif;font-weight:700;font-size:48px;color:var(--ink)}
.welcome p{width:690px;margin:16px auto 0;font-size:14px;line-height:27px;color:#666}
/* feature rows */
.feature-text{position:absolute;width:600px;height:365px;background:linear-gradient(90deg,#0b0b0b,#2a2a2a)}
.feature-text.rev{background:linear-gradient(90deg,#2c2c2c,#0b0b0b)}
.feature-text h2{position:absolute;left:109px;top:64px;font-family:'Cinzel',serif;font-weight:700;font-size:34px;color:#fff}
.feature-text .bar{position:absolute;left:93px;top:71px;width:4px;height:30px;background:var(--gold)}
.feature-text p{position:absolute;left:109px;top:112px;width:380px;font-size:14px;line-height:27px;color:#ddd}
.photo{position:absolute;width:600px;height:365px}
/* contact */
.contact{position:absolute;left:0;top:1989px;width:1200px;height:656px}
.contact-map{position:absolute;left:80px;top:50px;width:1040px;height:560px;background:radial-gradient(ellipse at center,#f4f1ea 0%,#fff 70%)}
.contact h2{position:absolute;width:100%;top:64px;text-align:center;font-family:'Cinzel',serif;font-weight:700;font-size:48px;color:var(--ink)}
.contact .lead{position:absolute;width:100%;top:126px;text-align:center;font-size:16px;color:#555}
.field{position:absolute;left:340px;width:520px;height:52px;border:1px solid #ddd;background:#fff;font-size:13px;color:#999;padding:17px 16px}
.field.active{border-color:var(--gold);color:var(--gold)}
.checks{position:absolute;top:2489px;left:0;width:1200px;display:flex;justify-content:center;gap:48px;font-size:14px;color:#444}
.checks span{display:flex;align-items:center;gap:26px}
.checks i{width:16px;height:16px;border:1px solid #bbb;display:inline-block}
/* footer */
.site-footer{position:absolute;left:0;top:2645px;width:1200px;height:221px;background:var(--footer)}
.footer-brand{position:absolute;left:86px;top:66px;display:flex;align-items:center;gap:14px}
.footer-brand .brand-mark{width:60px;height:60px}
.footer-brand .brand-name{font-size:36px;line-height:38px;color:var(--gold)}
.social{position:absolute;right:78px;top:44px;display:flex;gap:6px}
.social span{width:42px;height:42px;border:1.5px solid var(--gold);border-radius:50%}
.footer-info{position:absolute;right:78px;top:104px;text-align:right;font-size:14px;line-height:23px;color:#999}
.footer-info .hl{color:var(--gold)}
.footer-info .copy{margin-top:9px}
.gold-strip{position:absolute;left:0;top:2866px;width:1200px;height:14px;background:var(--gold-band)}
</style>
</head>
<body>

<header class="site-header">
  <div class="brand"><span class="brand-mark"></span><span class="brand-name">CALDER<br>HOMES</span></div>
  <div class="nav-home">HOME</div>
  <nav class="abs" style="left:708px;top:44px;font-size:15px;color:#333;letter-spacing:.5px">INVEST</nav>
  <nav class="abs" style="left:801px;top:44px;font-size:15px;color:#333;letter-spacing:.5px">SELL</nav>
  <nav class="abs" style="left:869px;top:44px;font-size:15px;color:#333;letter-spacing:.5px">ABOUT US</nav>
  <nav class="abs" style="left:981px;top:44px;font-size:15px;color:#333;letter-spacing:.5px">CONTACT US</nav>
  <svg class="abs" style="left:1106px;top:45px" width="16" height="16" viewBox="0 0 16 16" aria-label="Search"><circle cx="6.5" cy="6.5" r="5" fill="none" stroke="#222" stroke-width="2.2"/><line x1="10.3" y1="10.3" x2="15" y2="15" stroke="#222" stroke-width="2.6"/></svg>
</header>

<section class="hero" role="img" aria-label="Two-storey suburban house at dusk with lit windows and a front lawn">
  <svg class="abs" style="left:0;top:0" width="1200" height="572" aria-hidden="true"><polygon points="0,0 126,0 615,572 0,572" fill="rgba(20,22,34,0.55)"/></svg>
  <h1 class="hero-title">CALDER<br>HOMES</h1>
  <p class="hero-sub">We ensure that whatever your property needs<br>are we deliver bespoke services for our clients</p>
  <div class="btn" style="left:78px;top:428px;width:192px;height:56px">CONTACT US</div>
  <div class="dots"><span></span><span></span><span class="on"></span><span></span><span></span></div>
</section>

<div class="call-band">
  <p>If you have any question for contact us Today !</p>
  <div class="call-num">
    <svg width="40" height="40" viewBox="0 0 40 40" aria-label="Phone"><circle cx="20" cy="20" r="18" fill="none" stroke="#1a1a1a" stroke-width="2.5"/><path d="M15 11c-3 2-3 8 1 14s8 8 10 6l1-2-4-3-2 1c-2-1-4-5-4-7l2-1-1-5z" fill="#1a1a1a"/></svg>
    01632 960482
  </div>
</div>

<section class="welcome">
  <h3>WELCOME TO</h3>
  <h2>CALDER HOMES</h2>
  <p>We are a property development and investment company that have our own portfolio and we are active investors who pride ourselves in expanding our business organically.</p>
  <p style="margin-top:18px">We ensure that whatever your property needs are we deliver bespoke services for our clients. For investors, sellers, landlords and tenants we bring knowledge to your next property decision, allowing you to make an informed decision.</p>
</section>
<div class="btn" style="left:504px;top:1138px;width:192px;height:57px">LEARN MORE</div>

<section class="feature-text" style="left:0;top:1260px">
  <span class="bar"></span>
  <h2>INVEST</h2>
  <p>We have our own portfolio and we are active investors, so our finger is on the pulse and we are currently looking for residential development investments &amp; commercial to residential conversions.</p>
  <div class="btn" style="left:109px;top:238px;width:187px;height:52px">LEARN MORE</div>
</section>
<div class="photo" style="left:600px;top:1260px;background:linear-gradient(135deg,#f2f2f0,#d9d6d0 60%,#8b8378)" role="img" aria-label="Couple on a sofa shaking hands with an adviser over house plans"></div>

<div class="photo" style="left:0;top:1625px;background:radial-gradient(circle at 50% 55%,#8a5a3a 0%,#d7a27c 35%,#cfcfcf 75%)" role="img" aria-label="Cupped hands holding a small model house on grass"></div>
<section class="feature-text rev" style="left:600px;top:1625px">
  <span class="bar"></span>
  <h2>SELL</h2>
  <p>We undertake the necessary market research to evaluate an option that works for all parties involved. We will help guide you to make an informed decision on how to gain the maximum realistic value.</p>
  <div class="btn" style="left:109px;top:236px;width:187px;height:52px">LEARN MORE</div>
</section>

<section class="contact">
  <div class="contact-map" role="img" aria-label="Faint dotted world map background"></div>
  <h2>CONTACT US</h2>
  <p class="lead">If you have any question for contact us Today !</p>
</section>
<div class="field active" style="top:2158px">Name *</div>
<div class="field" style="top:2219px">Phone *</div>
<div class="field" style="top:2280px">Email *</div>
<div class="field" style="top:2341px;height:113px">Message*</div>
<div class="checks"><span>SELLERS <i></i></span><span>RENTERS <i></i></span><span>INVESTORS <i></i></span></div>
<div class="btn" style="left:507px;top:2526px;width:187px;height:52px">SUBMIT</div>

<footer class="site-footer">
  <div class="footer-brand"><span class="brand-mark"></span><span class="brand-name">CALDER<br>HOMES</span></div>
  <div class="social"><span aria-label="Social link"></span><span aria-label="Social link"></span><span aria-label="Social link"></span></div>
  <div class="footer-info">
    01632 960482 | <span class="hl">hello@calderhomes.example</span><br>
    12 Larkfield Lane, Ashworth, Westshire, AW1 4QT
    <div class="copy">©<span class="hl">CALDER HOMES</span> - 2019 All Rights Reserved.</div>
  </div>
</footer>
<div class="gold-strip"></div>

</body>
</html>
```